Sudden Tides "Lantern Road" New Single Cover

Create cover artwork for the band Sudden Tides' new single "Lantern Road" being released early 2020. Style, font and graphics to be consistent with band's previous releases and overall brand identity. Visit www.suddentidesband.example and our Spotify page https://music.example.net/artist/7QzWpLx3RtVnKd8e2YbHcJ?si=MUrTgKa4PLe7skvWq2AmZd to view our previous releases and overall brand identity. Some examples attached as well. We are looking for someone to work with on future projects as well.

Lyrics are here: https://docs.example.org/document/d/3KTp9wrn_2ZQa8eXb4Lo_fimH7C5m83Jz4Pd70hrtVcA/edit

Music is here: https://audiostream.example.com/suddentides/lantern-road/s-pzkwa

Font styles to use
Sans Serif

Colors

Designer to choose colors to be used in the design.

Requirements
Must have
• Must be consistent with current brand identity and with prior album / single art.

```html
<!DOCTYPE html>
<html lang="en">
<head>
<meta charset="utf-8">
<title>Sudden Tides – Lantern Road</title>
<link rel="stylesheet" href="https://fonts.googleapis.com/css2?family=Josefin+Sans:wght@400;700&display=swap">
<style>
  :root {
    --ink-teal: #4787a0;
    --band-edge: #4d93b3;
    --sun-yellow: #ffd21c;
    --logo-yellow: #f2e63a;
    --yellow: #ffc800;
    --green: #6ec1a0;
    --lime: #c6d843;
    --salmon: #f08c6e;
    --sky: #5bc4ec;
    --pink: #f08fae;
  }
  html, body {
    margin: 0;
    width: 1200px;
    height: 1200px;
    overflow: hidden;
    background: var(--ink-teal);
  }
  .cover {
    position: relative;
    width: 1200px;
    height: 1200px;
    background: var(--ink-teal);
    font-family: "Josefin Sans", sans-serif;
    overflow: hidden;
  }
  .sunburst {
    position: absolute;
    left: 509px;
    top: 141px;
    width: 180px;
    height: 180px;
    border-radius: 50%;
    background: radial-gradient(circle, rgba(255,210,28,0.12) 0 22%, rgba(255,210,28,0.75) 24% 30%, rgba(255,210,28,0.4) 46%, rgba(255,210,28,0) 70%);
  }
  .title-band {
    position: absolute;
    left: 0;
    top: 431px;
    width: 1200px;
    height: 333px;
    background: linear-gradient(90deg,
      var(--band-edge) 0%,
      var(--yellow) 20%,
      var(--green) 33%,
      var(--lime) 45%,
      var(--salmon) 57%,
      var(--sky) 69%,
      var(--pink) 80%,
      var(--band-edge) 100%);
  }
  .title {
    position: absolute;
    left: 0;
    top: 431px;
    width: 1200px;
    height: 333px;
    margin: 0;
    display: flex;
    flex-direction: column;
    justify-content: center;
    align-items: center;
    color: var(--ink-teal);
    font-weight: 700;
    font-size: 150px;
    line-height: 150px;
    letter-spacing: 10px;
    text-align: center;
  }
  .title-line {
    display: block;
    padding-top: 20px;
  }
  .band-name {
    position: absolute;
    left: 0;
    right: 0;
    top: 940px;
    margin: 0;
    text-align: center;
    color: var(--logo-yellow);
    font-weight: 400;
    font-size: 44px;
    letter-spacing: 6px;
    line-height: 50px;
  }
</style>
</head>
<body>
  <main class="cover">
    <div class="sunburst" role="img" aria-label="Yellow sunburst emblem"></div>

    <div class="title-band" role="img" aria-label="Band of bright coloured blocks behind the single title"></div>
    <h1 class="title">
      <span class="title-line">LANTERN</span>
      <span class="title-line">ROAD</span>
    </h1>

    <p class="band-name">SUDDEN<br>TIDES</p>
  </main>
</body>
</html>
```